" A vanta soluções de conexão é uma empresa de serviços que presta suporte e gerenciamento técnico para provedores de internet e outras empresas. "

```html
<!DOCTYPE html>
<html lang="pt-BR">
<head>
<meta charset="UTF-8">
<title>Vanta Soluções de Conexão — Papel Timbrado</title>
<link href="https://fonts.googleapis.com/css2?family=Montserrat:wght@500;700;800&display=swap" rel="stylesheet">
<style>
  :root {
    --navy: #1d2e5c;
    --teal: #2bb4c1;
    --teal-light: #7fd6dd;
    --paper: #ffffff;
    --backdrop: #e9eaec;
    --ghost: #f1f2f3;
    --ink: #3a4258;
  }
  * { margin: 0; padding: 0; box-sizing: border-box; }
  html, body { width: 1200px; height: 1200px; overflow: hidden; }
  body {
    background: var(--backdrop);
    font-family: "Montserrat", sans-serif;
    display: flex;
    align-items: center;
    justify-content: center;
  }
  .letterhead {
    position: relative;
    width: 778px;
    height: 1100px;
    background: var(--paper);
    box-shadow: 0 6px 24px rgba(0,0,0,0.12);
    overflow: hidden;
  }
  .brand {
    position: absolute;
    top: 58px;
    left: 62px;
    display: flex;
    align-items: center;
    gap: 12px;
  }
  .brand-mark {
    width: 30px;
    height: 30px;
    background: var(--teal);
  }
  .brand-name {
    font-weight: 800;
    font-size: 30px;
    letter-spacing: 1px;
    color: var(--navy);
    line-height: 1;
  }
  .brand-tagline {
    display: block;
    font-weight: 700;
    font-size: 8.5px;
    letter-spacing: 0.6px;
    color: var(--navy);
    margin-top: 3px;
    text-transform: uppercase;
  }
  .ghost-square {
    position: absolute;
    top: 380px;
    left: 289px;
    width: 200px;
    height: 200px;
    background: var(--ghost);
  }
  .footer {
    position: absolute;
    left: 62px;
    right: 62px;
    bottom: 46px;
    display: flex;
    justify-content: space-between;
    align-items: center;
    font-size: 10.5px;
    font-weight: 500;
    color: var(--ink);
    line-height: 1.35;
  }
  .contact { display: flex; align-items: center; gap: 6px; }
  .contact svg { width: 16px; height: 16px; flex: none; }
  .social { display: flex; align-items: center; gap: 6px; }
  .social-dot { width: 14px; height: 14px; border-radius: 50%; background: var(--teal); }
  .band {
    position: absolute;
    left: 0; right: 0; bottom: 0;
    height: 22px;
    background: linear-gradient(90deg, var(--teal-light), var(--teal) 50%, var(--teal-light));
  }
  .band::before {
    content: "";
    position: absolute;
    left: 0; right: 0; top: -6px;
    height: 3px;
    background: var(--teal);
    opacity: 0.5;
  }
</style>
</head>
<body>
  <main class="letterhead">
    <header class="brand">
      <span class="brand-mark"></span>
      <div>
        <span class="brand-name">VANTA</span>
        <span class="brand-tagline">soluções de conexão</span>
      </div>
    </header>

    <div class="ghost-square" aria-hidden="true"></div>

    <footer class="footer">
      <div class="contact">
        <svg viewBox="0 0 16 16"><circle cx="8" cy="8" r="8" fill="#2bb4c1"/><path d="M5.5 4.5l1.5 0 .7 2-1 .8a5 5 0 0 0 2 2l.8-1 2 .7 0 1.5c-3.5.3-6.3-2.5-6-6z" fill="#fff"/></svg>
        <span>(91) 3047-2281<br>(91) 98214-6075</span>
      </div>
      <div class="contact">
        <svg viewBox="0 0 16 16"><circle cx="8" cy="8" r="8" fill="#2bb4c1"/><path d="M8 3.5a3 3 0 0 0-3 3c0 2.2 3 6 3 6s3-3.8 3-6a3 3 0 0 0-3-3zm0 4.2a1.2 1.2 0 1 1 0-2.4 1.2 1.2 0 0 1 0 2.4z" fill="#fff"/></svg>
        <span>Rua das Acácias, 412 | Centro<br>CEP: 66015-230 | Cidade/UF</span>
      </div>
      <div class="contact">
        <svg viewBox="0 0 16 16"><circle cx="8" cy="8" r="8" fill="#2bb4c1"/><rect x="4" y="5" width="8" height="6" rx="1" fill="#fff"/><path d="M4.3 5.4L8 8.3l3.7-2.9" stroke="#2bb4c1" stroke-width="0.9" fill="none"/></svg>
        <span>contato@vantaconexao.com<br>www.vantaconexao.com.br</span>
      </div>
      <div class="social">
        <span class="social-dot"></span>
        <span>vanta.conexao</span>
      </div>
    </footer>

    <div class="band"></div>
  </main>
</body>
</html>
```